DEADLINE 4 JAN 2015 - Drama Movie POSTER

Title of movie " KORAL " - in English SUNSET, Koral is a Sanskrit language, we expect the font to be a little towards that influence ( ethnic )

STORY:
This movie is about one girl's life survival, played by actress ( MIRA HALVORSEN ) fighting her life out of leukemia, deceived in relationship, denying love, searching for her birth father and later kidnapped but saved.

GENRE:
Its a drama with twist of thriller in the end.

COUNTRIES INVOLVED:
Phuket islands in Thailand and Bali and city scenes in Jakarta, Singapore and Istanbul.

We upload photos of actors involved, and we CAN have them on the poster, you can be creative but yet keep it elegant and sophisticated, the movie is for an upmarket. So we dont want too much color. Sunset color mixed with dark or black is nice.

Look forward to see you creative design! Thanks so much!

ACTORS NAME:
- Rudy Pelangi
- Kit B Mayhew
- Tobias Wen
- K Trax
- Hendra Sulut
- Mateo Brunvelli
- Mira Halvorsen
- Sari Lynne
- Ayu Kemalasari
- Ruqaya
- Felix Moro
- Yos Latuheru
- Faustino Medeira

TITLE OF MOVIE:
KORAL - " we love, we cry, we fall but we survive "

If you need sample of promotional trailer, please request with your email address.

Please Check our Brief as we have edited and add some more information needed.Many thanks and look forward to your arts.Warm Regards,KorvoStage Pictures Added Sunday, December 21, 2014

Investors, Young Adults and Adults Crowds

Movie

• Ethnic

• Movie title and Quotes : " we love, we cry, we fall but we survive "
• ( with or without logo ) Production House:
• KorvoStage Pictures in collaboration with Glimmerax.Inc
• Director's name:
• Budi Sastro & Teguh Rambukasih
• Actor Names in order:
• Rudy Pelangi, Ktrax, Sari Lynne, Hendra Sulut, Tobias Wen, Ayu Kemalasari, Felix Moro, Kit B Mayhew, Ruqaya, Mateo Brunvelli, Yos Latuheru, Mira Halvorsen, Faustino Medeira
• Poster influences: Fallow Ridge
• If you want to use the same idea, you can use a silhouette of a girl
• from one of mira halvorsen's picture WITHOUT exposing her face

```html
<!DOCTYPE html>
<html lang="en">
<head>
<meta charset="utf-8">
<title>Koral – Movie Poster</title>
<link rel="stylesheet" href="https://fonts.googleapis.com/css2?family=Yatra+One&family=Cinzel:wght@400&family=Arimo:wght@400;700&display=swap">
<style>
  :root {
    --page-bg: #e9e7e4;
    --sky-top: #5a3208;
    --sky-mid: #b8650f;
    --sky-glow: #f2a323;
    --sea-dark: #1a0d05;
    --figure-dark: #0d0603;
    --title-gold: #f5cf4a;
    --credit-tan: #c9a46a;
    --note-cream: #f4e6d2;
    --logo-white: #ffffff;
    --logo-ink: #2a2a2a;
  }
  * { margin: 0; padding: 0; box-sizing: border-box; }
  html, body { width: 1200px; height: 1148px; overflow: hidden; }
  body {
    background: var(--page-bg);
    position: relative;
    font-family: 'Arimo', Arial, sans-serif;
  }
  .poster {
    position: absolute;
    left: 200px; top: 28px;
    width: 800px; height: 1092px;
    overflow: hidden;
    background: var(--sea-dark);
  }
  .poster-photo {
    position: absolute; inset: 0;
    background:
      radial-gradient(ellipse 260px 160px at 78% 56%, rgba(255,214,110,.95), rgba(242,163,35,.55) 45%, rgba(242,163,35,0) 100%),
      linear-gradient(180deg, var(--sky-top) 0%, #7a430a 20%, var(--sky-mid) 42%, var(--sky-glow) 56%, #6a3207 63%, #2a1406 70%, var(--sea-dark) 100%);
  }
  .figure-area {
    position: absolute;
    left: 60px; top: 150px;
    width: 330px; height: 942px;
    background: linear-gradient(180deg, var(--figure-dark) 0%, var(--figure-dark) 100%);
    border-radius: 150px 150px 0 0;
    opacity: .92;
  }
  .studio-badge {
    position: absolute;
    left: 488px; top: 3px;
    width: 140px; height: 116px;
    background: var(--logo-white);
    display: flex; flex-direction: column; align-items: center; justify-content: center;
    gap: 8px;
  }
  .studio-badge .mark {
    width: 34px; height: 34px; border-radius: 50%;
    background: var(--logo-ink);
  }
  .studio-badge .name {
    font-size: 13px; font-weight: 700;
    color: var(--logo-ink);
    text-align: center; line-height: 1.15;
  }
  .collab-note {
    position: absolute;
    left: 478px; top: 127px; width: 160px;
    text-align: center;
    font-size: 10px; letter-spacing: .3px;
    color: var(--note-cream);
  }
  .partner-name {
    position: absolute;
    left: 478px; top: 165px; width: 160px;
    text-align: center;
    font-size: 15px; font-weight: 700;
    color: var(--note-cream);
  }
  .title-rule {
    position: absolute;
    left: 150px; top: 700px;
    width: 530px; height: 7px;
    background: var(--title-gold);
  }
  .film-title {
    position: absolute;
    left: 140px; top: 660px;
    width: 560px;
    font-family: 'Yatra One', Georgia, serif;
    font-size: 190px; line-height: 1;
    font-weight: 400;
    color: var(--title-gold);
    letter-spacing: 4px;
    text-align: center;
  }
  .tagline {
    position: absolute;
    left: 168px; top: 880px;
    font-size: 18px;
    color: var(--title-gold);
  }
  .directors {
    position: absolute;
    left: 175px; top: 922px;
    font-family: 'Cinzel', 'Times New Roman', serif;
    font-size: 20px;
    color: var(--credit-tan);
    letter-spacing: .5px;
    white-space: nowrap;
  }
  .cast {
    position: absolute;
    left: 150px; top: 960px; width: 580px;
    font-size: 12px; line-height: 1.3;
    color: var(--credit-tan);
    text-align: center;
    white-space: nowrap;
  }
</style>
</head>
<body>
  <main class="poster">
    <div class="poster-photo" role="img" aria-label="Photograph of a sunset over the sea and distant mountains"></div>
    <div class="figure-area" role="img" aria-label="Dark silhouette of a girl seen from the side, face not shown"></div>

    <div class="studio-badge">
      <span class="mark"></span>
      <span class="name">KorvoStage<br>Pictures</span>
    </div>
    <p class="collab-note">IN COLLABORATION WITH</p>
    <p class="partner-name">Glimmerax Inc.</p>

    <div class="title-rule"></div>
    <h1 class="film-title">koral</h1>
    <p class="tagline">we love, we cry, we fall but we survive</p>
    <p class="directors">DIRECTORS : BUDI SASTRO &amp; TEGUH RAMBUKASIH</p>
    <p class="cast">
      RUDY PELANGI, KTRAX, SARI LYNNE, HENDRA SULUT, TOBIAS WEN, AYU KEMALASARI,<br>
      FELIX MORO, KIT B MAYHEW, RUQAYA, MATEO BRUNVELLI, YOS LATUHERU,<br>
      MIRA HALVORSEN, FAUSTINO MEDEIRA
    </p>
  </main>
</body>
</html>
```